Upsell Vertical Banner Ad Design For B2B Marketing Agency Vertical 768px × 1180px IS THE SIZE

I need a banner made for my website www.brightlanepromotionhub.biz This banner will be an upsell advertisement for after someone signs up for my monthly program. When they login to their account for the 1st time I will give them the chance to upgrade their account to our annual program with just one click.

this is a page that upsells it currently to give you an idea how we market ourselves:
https://tlpx.pagevault-example.com/page/tlp-annual-upsell

Use this content:

Are You Ready To Commit To Taking Your Business To The Next Level?

Because We're In This For The Long-Haul and Dedicated To Your Success...

Save $300 By Upgrading To An Annual Membership And Pay Only $74/mth

((BUTTON))Yes, Upgrade My Plan Right Now!

*Must prepay the full year at only $898/yr!

Target Market(s)

business owners

Industry/Entity Type

Marketing

Requirements
Must have
• 768px × 1180px IS THE SIZE vertical

Use this content:

Nice to have
• Use this content:

Should not have
• Use this content:

```html
<!DOCTYPE html>
<html lang="en">
<head>
<meta charset="utf-8">
<title>Bright Lane Promotion Hub – Annual Upgrade</title>
<link href="https://fonts.googleapis.com/css2?family=Roboto:wght@400;500;700;900&family=Roboto+Condensed:wght@400;700&display=swap" rel="stylesheet">
<style>
  :root {
    --blue: #1d6fd0;
    --blue-deep: #175cb3;
    --blue-light: #4f95e3;
    --navy: #0b1f5c;
    --white: #ffffff;
    --yellow: #ffe600;
    --lime: #d7f542;
    --green-top: #b6ec3c;
    --green-bottom: #35c24a;
    --brand: #1a55a8;
  }
  html, body { margin: 0; padding: 0; overflow: hidden; }
  body { width: 783px; height: 1200px; background: var(--white); }
  .banner {
    position: relative;
    width: 783px;
    height: 1200px;
    overflow: hidden;
    font-family: "Roboto", sans-serif;
    background: var(--blue);
  }
  .backdrop { position: absolute; inset: 0; }
  .brand {
    position: absolute;
    top: 58px; left: 0; width: 100%;
    display: flex; justify-content: center; align-items: center; gap: 16px;
  }
  .brand-dot { width: 44px; height: 44px; border-radius: 50%; background: var(--brand); }
  .brand-name {
    font-family: "Roboto Condensed", sans-serif;
    font-weight: 700; font-size: 34px; letter-spacing: 1px;
    color: var(--brand); text-transform: uppercase;
  }
  .content {
    position: absolute; left: 0; top: 488px; width: 100%;
    text-align: center; color: var(--white);
  }
  .headline-lead { margin: 0; font-weight: 400; font-size: 66px; line-height: 1; }
  .headline-sub { margin: 14px 0 0; font-weight: 400; font-size: 37px; line-height: 1.1; }
  .headline-box {
    display: inline-block; margin-top: 20px;
    background: var(--navy); color: var(--yellow);
    font-weight: 700; font-size: 58px; line-height: 1;
    padding: 9px 26px 11px;
  }
  .promise {
    margin: 42px 0 0; color: var(--navy);
    font-weight: 500; font-size: 33px; line-height: 1.2;
  }
  .offer { margin: 30px 0 0; font-weight: 500; font-size: 30px; line-height: 1.15; }
  .offer-price { display: block; color: var(--lime); }
  .cta {
    display: inline-block; margin-top: 48px;
    padding: 14px 30px;
    background: linear-gradient(var(--green-top), var(--green-bottom));
    border-radius: 6px;
    color: var(--navy); font-weight: 500; font-size: 24px;
    text-decoration: none;
    box-shadow: 0 4px 8px rgba(0,0,0,0.25);
  }
  .fineprint {
    position: absolute; left: 0; width: 100%; top: 1114px;
    text-align: center; color: var(--white); font-size: 19px; margin: 0;
  }
</style>
</head>
<body>
  <div class="banner">
    <svg class="backdrop" width="783" height="1200" viewBox="0 0 783 1200" aria-hidden="true">
      <rect width="783" height="1200" fill="var(--blue)"/>
      <path d="M783 0 L783 300 C640 300 520 290 380 330 L783 250 Z" fill="var(--blue-deep)"/>
      <path d="M0 0 H783 V265 C560 240 240 300 0 470 Z" fill="var(--blue-light)"/>
      <path d="M0 0 H783 V235 C540 215 220 285 0 445 Z" fill="var(--white)"/>
    </svg>

    <div class="brand">
      <span class="brand-dot"></span>
      <span class="brand-name">Bright Lane Promotion Hub</span>
    </div>

    <div class="content">
      <h1 class="headline-lead">Are You Ready</h1>
      <p class="headline-sub">To Commit To Taking Your Business</p>
      <div class="headline-box">To The Next Level?</div>
      <p class="promise">Because We're In This For The Long-Haul and<br>Dedicated To Your Success...</p>
      <p class="offer">Save $300 By Upgrading To An Annual Membership
        <span class="offer-price">And Pay Only $74/mth</span></p>
      <a class="cta" href="#">Yes, Upgrade My Plan Right Now!</a>
    </div>

    <p class="fineprint">*Must prepay the full year at only $898/yr!</p>
  </div>
</body>
</html>
```